Tom Pelling Personal Website Yoga Teacher and Personal Fitness Trainer

Let's pick a WORDPRESS theme that can work with Video Bckground. I would like a website design to look like some of nice Squarespace themes.
I would like to have a Video background of me teaching. I can provide video. Please view my current Wordpress site: www.tompelling.example. I also have new logo. See file tpel1.png

Reason: I am guaranteeing this project because i believe designers can deliver. I am extending 5 days because the homepage image/video slider is intricate and takes a bit of time. I have provided details, images, video etc. in Dropbox. Tx

Target Market(s)

All people needing & wanting personal help (they can trust and feel safe and nurtured) for their health (wellness, nutrition, fitness, exercise). And people wanting extraordinary yoga teaching.

Industry/Entity Type

Fitness

Number of Pages Required

5+ page

Colors
9bcb3b
add136
cadf82
eaf2ce

Requirements
Must have
• Template that can use a video background
Nice to have
• Need to show good image gallery and testimonial videos

```html
<!DOCTYPE html>
<html lang="en">
<head>
<meta charset="utf-8">
<title>Tom Pelling – Yoga &amp; Wellness</title>
<link href="https://fonts.googleapis.com/css2?family=Open+Sans:wght@300;400;600;700&family=Great+Vibes&display=swap" rel="stylesheet">
<style>
  :root {
    --green: #9bcb3b;
    --green-dark: #7fae1f;
    --lime: #add136;
    --lime-soft: #cadf82;
    --lime-pale: #eaf2ce;
    --ink: #111111;
    --text: #666666;
    --rule: #e2e2e2;
    --white: #ffffff;
  }
  * { box-sizing: border-box; margin: 0; padding: 0; }
  html, body { width: 1200px; height: 2663px; overflow: hidden; background: var(--white); }
  body { position: relative; font-family: "Open Sans", Arial, sans-serif; color: var(--text); }

  .site-header { position: absolute; left: 97px; top: 0; width: 997px; height: 88px; }
  .brand { position: absolute; left: 0; top: 14px; display: flex; align-items: center; gap: 10px; }
  .brand-dot { width: 40px; height: 40px; border-radius: 50%; background: var(--green); }
  .brand-text { display: flex; flex-direction: column; }
  .brand-name { font-size: 22px; font-weight: 700; color: var(--green-dark); letter-spacing: 0.5px; line-height: 1; }
  .brand-tag { font-size: 9px; color: var(--green-dark); margin-top: 4px; }
  .main-nav { position: absolute; right: 0; top: 33px; display: flex; gap: 22px; align-items: center; }
  .main-nav a { font-size: 13px; color: var(--ink); text-decoration: none; }
  .search-icon { width: 20px; height: 20px; margin-left: 6px; }

  .hero { position: absolute; left: 97px; top: 88px; width: 997px; height: 650px; }
  .hero-media { position: absolute; inset: 0;
    background: linear-gradient(180deg, #d9cfc0 0%, #cbb48d 45%, #b98a45 72%, #8a5a22 100%); }
  .hero-content { position: absolute; left: 0; right: 0; top: 232px; text-align: center; color: var(--white); }
  .hero-title { font-size: 44px; font-weight: 400; line-height: 1.2; }
  .hero-lead { font-size: 15px; line-height: 26px; width: 700px; margin: 8px auto 0; }
  .hero-button { display: inline-block; margin-top: 22px; width: 164px; height: 41px; line-height: 39px;
    border: 1px solid var(--white); color: var(--white); font-size: 17px; text-decoration: none; }
  .slider-arrow { position: absolute; top: 395px; width: 40px; height: 40px; }
  .slider-arrow.prev { left: 28px; }
  .slider-arrow.next { left: 1117px; }

  .section-title { position: absolute; left: 0; width: 1200px; text-align: center;
    font-size: 34px; font-weight: 300; color: var(--ink); letter-spacing: 0.5px; }
  .section-title strong { font-weight: 700; }
  .section-lead { position: absolute; left: 0; width: 1200px; text-align: center;
    font-size: 15px; line-height: 28px; color: var(--text); }
  .section-lead p { width: 740px; margin: 0 auto; }
  .section-lead.narrow p { width: 700px; }
  .read-more { display: block; color: var(--green); font-size: 15px; text-decoration: none; }
  .divider { position: absolute; left: 97px; width: 997px; height: 1px; background: var(--rule); }

  .tile { position: absolute; }
  .tile-fruit { background: linear-gradient(135deg, #d8362a, #e9b52b 45%, #3f4a8c); }
  .tile-group { background: linear-gradient(180deg, #b59a86, #6f7a5b 60%, #3a3a3a); }
  .tile-water { background: linear-gradient(180deg, #3d7fb5, #235b91); }
  .tile-stretch { background: linear-gradient(180deg, #c9b8a8, #4f6b3c 55%, #2f4a24); }
  .tile-feature { background: linear-gradient(180deg, #c5d58c, #a9c257); }
  .tile-feature .overlay { position: absolute; inset: 0; background: rgba(155,203,59,0.82);
    display: flex; flex-direction: column; align-items: center; justify-content: center; color: var(--white); }
  .overlay-label { font-size: 17px; font-weight: 600; margin-top: 10px; }

  .video { position: absolute; display: flex; align-items: center; justify-content: center; }
  .video-class { background: linear-gradient(135deg, #7a6a5c, #c2a68e 50%, #3c3a38); }
  .video-pose { background: linear-gradient(180deg, #e6d2a8, #c89a52 70%, #6b4a2a); }
  .video-studio { background: linear-gradient(180deg, #a8b0a4, #6f7a70 55%, #3f4a42); }
  .play { width: 52px; height: 52px; }

  .subscribe { position: absolute; left: 97px; top: 2393px; width: 997px; height: 193px; background: var(--lime); }
  .subscribe-title { position: absolute; left: 182px; top: 44px; color: var(--white); font-size: 37px; font-weight: 400; line-height: 1; }
  .subscribe-script { position: absolute; left: 178px; top: 90px; color: var(--white); font-family: "Great Vibes", cursive; font-size: 52px; line-height: 1; }
  .email-field { position: absolute; left: 413px; top: 48px; width: 528px; height: 39px; border: 2px solid var(--white);
    color: var(--white); font-size: 13px; line-height: 35px; padding-left: 14px; text-transform: uppercase; }
  .subscribe-button { position: absolute; left: 413px; top: 104px; width: 528px; height: 43px; background: var(--white);
    color: var(--green); font-size: 13px; line-height: 43px; text-align: center; text-transform: uppercase; }

  .site-footer { position: absolute; left: 97px; top: 2605px; width: 997px; height: 26px; }
  .copyright { position: absolute; left: 4px; top: 3px; font-size: 14px; color: var(--ink); }
  .social { position: absolute; right: 0; top: 0; display: flex; gap: 10px; }
  .social span { width: 22px; height: 22px; border-radius: 50%; }
  .s1 { background: #3b5998; } .s2 { background: #29a9e1; } .s3 { background: #0e76a8; } .s4 { background: #dd4b39; } .s5 { background: #cb2027; }
</style>
</head>
<body>

<header class="site-header">
  <div class="brand">
    <span class="brand-dot"></span>
    <div class="brand-text">
      <span class="brand-name">TOM PELLING</span>
      <span class="brand-tag">Guiding a healthier life</span>
    </div>
  </div>
  <nav class="main-nav">
    <a href="#">Home</a><a href="#">About</a><a href="#">Blog</a><a href="#">Clients</a><a href="#">Contact</a>
    <a href="#">Media</a><a href="#">Nutrion</a><a href="#">Schedule/Classes</a><a href="#">Services</a>
    <svg class="search-icon" viewBox="0 0 20 20"><circle cx="8" cy="8" r="5.5" fill="none" stroke="#9bcb3b" stroke-width="2.2"/><line x1="12" y1="12" x2="18" y2="18" stroke="#9bcb3b" stroke-width="2.6" stroke-linecap="round"/></svg>
  </nav>
</header>

<section class="hero">
  <div class="hero-media" role="img" aria-label="Yoga teacher kneeling on a mat in a sunlit studio"></div>
  <div class="hero-content">
    <h1 class="hero-title">Leader of Yoga Teacher Training</h1>
    <p class="hero-lead">Are you at a decision point in your life, where wellness has become a priority and you are seeking additional support to reach your goals?</p>
    <a class="hero-button" href="#">Learn More</a>
  </div>
</section>
<svg class="slider-arrow prev" viewBox="0 0 40 40"><circle cx="20" cy="20" r="17" fill="none" stroke="#9bcb3b" stroke-width="3"/><path d="M23 12 L15 20 L23 28 Z" fill="#9bcb3b"/></svg>
<svg class="slider-arrow next" viewBox="0 0 40 40"><circle cx="20" cy="20" r="17" fill="none" stroke="#9bcb3b" stroke-width="3"/><path d="M17 12 L25 20 L17 28 Z" fill="#9bcb3b"/></svg>

<h2 class="section-title" style="top:795px">WELCOME TO <strong>TOM PELLING</strong></h2>
<div class="section-lead narrow" style="top:860px">
  <p>Are you at a decision point in your life, where wellness has become a priority and you are seeking additional support to reach your goals? Crossroads Path Wellness offers a unique, exciting innovation in wellness and nutrition: health coaching. As a Certified Health Coach, I...</p>
  <a class="read-more" href="#">READ MORE &gt;&gt;</a>
</div>

<div class="divider" style="top:1018px"></div>

<h2 class="section-title" style="top:1063px">IMAGE <strong>GALLERY</strong></h2>
<div class="section-lead" style="top:1114px">
  <p>Lorem Ipsum is simply dummy text of the printing and typesetting industry. Lorem Ipsum has been the industry's standard dummy text ever since the 1500s, scracimen book.</p>
</div>

<div class="tile tile-fruit" style="left:97px;top:1197px;width:320px;height:226px" role="img" aria-label="Fresh fruit and vegetables"></div>
<div class="tile tile-group" style="left:438px;top:1197px;width:319px;height:226px" role="img" aria-label="Group of yoga students"></div>
<div class="tile tile-water" style="left:97px;top:1444px;width:320px;height:227px" role="img" aria-label="Yoga pose in the sea"></div>
<div class="tile tile-stretch" style="left:438px;top:1444px;width:319px;height:227px" role="img" aria-label="Assisted stretch outdoors"></div>
<div class="tile tile-feature" style="left:777px;top:1197px;width:317px;height:474px" role="img" aria-label="Students in a standing yoga pose">
  <div class="overlay">
    <svg width="44" height="44" viewBox="0 0 44 44"><circle cx="22" cy="22" r="19" fill="none" stroke="#fff" stroke-width="3"/><path d="M22 12v20M12 22h20" stroke="#fff" stroke-width="4"/></svg>
    <span class="overlay-label">Benefits At Any Age</span>
  </div>
</div>

<div class="divider" style="top:1738px"></div>

<h2 class="section-title" style="top:1787px">OUR <strong>TESTIMONIALS</strong></h2>
<div class="section-lead" style="top:1841px">
  <p>Lorem Ipsum is simply dummy text of the printing and typesetting industry. Lorem Ipsum has been the industry's standard dummy text ever since the 1500s, scracimen book.</p>
</div>

<div class="video video-class" style="left:97px;top:1924px;width:334px;height:187px" role="img" aria-label="Testimonial video of a yoga class">
  <svg class="play" viewBox="0 0 52 52"><circle cx="26" cy="26" r="23" fill="none" stroke="#fff" stroke-width="2.5"/><path d="M21 16 L36 26 L21 36 Z" fill="#fff"/></svg>
</div>
<div class="video video-pose" style="left:97px;top:2130px;width:334px;height:191px" role="img" aria-label="Testimonial video of a triangle pose">
  <svg class="play" viewBox="0 0 52 52"><circle cx="26" cy="26" r="23" fill="none" stroke="#fff" stroke-width="2.5"/><path d="M21 16 L36 26 L21 36 Z" fill="#fff"/></svg>
</div>
<div class="video video-studio" style="left:450px;top:1924px;width:644px;height:397px" role="img" aria-label="Testimonial video of a studio class">
  <svg class="play" style="width:60px;height:60px" viewBox="0 0 52 52"><circle cx="26" cy="26" r="23" fill="none" stroke="#fff" stroke-width="2.5"/><path d="M21 16 L36 26 L21 36 Z" fill="#fff"/></svg>
</div>

<section class="subscribe">
  <div class="subscribe-title">SUBSCRIBE</div>
  <div class="subscribe-script">Newsletter !</div>
  <div class="email-field">Enter email address...</div>
  <div class="subscribe-button">Subscribe</div>
</section>

<footer class="site-footer">
  <span class="copyright">© 2015 All rights reserved.</span>
  <div class="social"><span class="s1"></span><span class="s2"></span><span class="s3"></span><span class="s4"></span><span class="s5"></span></div>
</footer>

</body>
</html>
```